Flyer Required for Economics Tuition business in Singapore

Require a 4-page, A4 bi-fold full colour flyer. To use attractive & vibrant colours. Can make use of colour schemes and design layouts from upcoming website revamp: http://lessonmaple.com/Website/
Target audience for the flyer will be 17 - 18 years old A Level students in Singapore studying in Junior Colleges.
I have attached the detailed design brief with the content required for the flyer as a file titled "Design Brief.docx" & also the logo for our business to be used in the flyer & optional photos that can be used in the flyer

```html
<!DOCTYPE html>
<html lang="en">
<head>
<meta charset="utf-8">
<title>LessonMaple Economics Tuition – Founder &amp; Testimonials Spread</title>
<link href="https://fonts.googleapis.com/css2?family=Bree+Serif&family=Open+Sans:wght@400;600;700&display=swap" rel="stylesheet">
<style>
:root{
  --backdrop:#e9e6e1;
  --blue:#1d6db5;
  --blue-deep:#155a9c;
  --navy:#1b3c7c;
  --orange:#f7941d;
  --lime:#b5d334;
  --green:#6fb23f;
  --yellow:#ffd200;
  --card-border:#e8336f;
  --card-text:#1a1a1a;
  --white:#ffffff;
}
*{box-sizing:border-box;margin:0;padding:0}
html,body{width:1200px;height:1000px;overflow:hidden;background:var(--backdrop)}
.spread{position:absolute;left:40px;top:100px;width:1120px;height:800px;overflow:hidden;box-shadow:0 6px 24px rgba(0,0,0,.25);font-family:"Open Sans",Arial,sans-serif}
.spread-bg{position:absolute;inset:0}
.founder-title{position:absolute;left:60px;top:22px;width:470px;text-align:center;font-family:"Bree Serif",Georgia,serif;font-size:25px;font-weight:400;color:var(--white)}
.founder-text{position:absolute;left:60px;top:64px;width:470px;color:var(--white);font-size:11px;line-height:1.28}
.founder-text h3{font-size:11.5px;font-weight:700;text-align:center;margin-top:5px}
.founder-text p{text-align:justify}
.photo{position:absolute;border:5px solid var(--yellow);border-radius:4px;background:linear-gradient(160deg,#d9d2c8,#8a7f78 55%,#3a3440)}
.photo-founder-class{left:28px;top:505px;width:370px;height:265px}
.photo-student-group{left:580px;top:14px;width:520px;height:250px;background:linear-gradient(170deg,#e6e2dc,#7a6f6a 50%,#2c2a36)}
.testimonials-title{position:absolute;left:600px;top:268px;width:490px;text-align:right;font-family:"Bree Serif",Georgia,serif;font-size:24px;font-weight:400;color:var(--white)}
.card-column{position:absolute;top:306px;height:484px;display:flex;flex-direction:column;gap:8px}
.col-left{left:590px;width:250px}
.col-right{left:848px;width:244px}
.card{flex:1 1 0;overflow:hidden;background:var(--white);border:3px solid var(--card-border);border-radius:10px;padding:6px 8px 5px;color:var(--card-text);font-size:9.4px;line-height:1.22;font-weight:600;display:flex;flex-direction:column;justify-content:space-between}
.card .small{font-size:7.6px;font-weight:400;line-height:1.25}
.card .author{text-align:right;font-size:9.4px;line-height:1.22}
</style>
</head>
<body>
<main class="spread">
  <svg class="spread-bg" width="1120" height="800" viewBox="0 0 1120 800" aria-hidden="true">
    <rect x="0" y="0" width="1120" height="800" fill="var(--blue)"/>
    <polygon points="420,0 560,0 560,800 500,800" fill="var(--blue-deep)"/>
    <rect x="0" y="0" width="28" height="800" fill="var(--orange)"/>
    <rect x="0" y="780" width="560" height="20" fill="var(--orange)"/>
    <rect x="120" y="780" width="160" height="20" fill="var(--blue-deep)"/>
    <rect x="280" y="780" width="120" height="20" fill="var(--lime)"/>
    <rect x="575" y="264" width="545" height="536" fill="var(--navy)"/>
    <polygon points="560,330 640,180 700,180 620,330 540,800 480,800" fill="var(--lime)"/>
    <polygon points="700,180 725,180 645,330 565,800 540,800 620,330" fill="var(--green)"/>
    <rect x="1098" y="300" width="22" height="500" fill="var(--orange)"/>
    <rect x="1040" y="6" width="80" height="5" fill="var(--orange)"/>
    <rect x="560" y="0" width="6" height="800" fill="#000" opacity=".08"/>
  </svg>

  <h1 class="founder-title">About our Programme Founder</h1>
  <section class="founder-text">
    <h3>Background</h3>
    <p>Mr Daniel Lim is the Programme Founder &amp; Managing Director for Economics At LessonMaple Pte Ltd. He also owns and manages BRIGHT Education Centre &amp; IdeaWorks Learning Centre.</p>
    <h3>Academic Qualifications</h3>
    <p>Mr Lim loves and specialises in Economics and he obtained his Bachelor of Arts in Economics from the Eastfield University (EU). He is also currently doing his Masters in Applied Economics at the Meridian Management University (MMU) and he intends to pursue further studies in Economics after his Masters.</p>
    <h3>Teaching Experience</h3>
    <p>Mr Lim has established a unique tuition programme under the name of Economics at LessonMaple since 2007. Each year he tutors about 150-200 on average and many of his students were top students in their classes and level for Economics. (read the testimonials!) That means more than a thousand students have gone through Mr Lim's intensive Economics tuition programme!</p>
    <h3>Style of Teaching</h3>
    <p>Mr Lim is different from other tutors because he employs a mixture of strategies to help the student excel. He thinks that for a student to excel in a subject, he must first be interested in the subject, and that's why Mr Lim tries to make his lessons interesting and relatable to the student. He also looks at the syllabus holistically and reverse engineers the methods to do well for the examination by ensuring that the appropriate right amount of content is covered without compromising on the quality of the learning. Through weekly discussions and looking at real-world problems, Mr Lim also helps his students discover the essential application skills that are required to score that Distinction in the A Levels.</p>
  </section>
  <div class="photo photo-founder-class" role="img" aria-label="Group photo of the founder seated with his economics class"></div>

  <div class="photo photo-student-group" role="img" aria-label="Cheerful group photo of students in a classroom"></div>
  <h2 class="testimonials-title">Testimonials From Students</h2>

  <div class="card-column col-left">
    <article class="card">
      <p class="quote">"Mr Lim really has all his students' interests at heart. He buys dinner for us, provides us with mini snacks and incentivises us with great rewards; he once even bought me flu medicine when I had a bad cold. thank you Mr Lim!"</p>
      <p class="author">Tan Mei Ling<br>Westbrook Junior College</p>
    </article>
    <article class="card">
      <p class="quote">"Mr Lim is a very friendly teacher who ensures that his students receive the best. He spends effort in preparing for lessons such as finding articles that are relevant to the subject and coming up with different ways to help us learn better."</p>
      <p class="author">Goh Wei Jie<br>St Aldric Junior College</p>
    </article>
    <article class="card">
      <p class="quote small">"Mr Lim's lessons are very engaging and fun. It's a very different and beneficial tuition style that will definitely benefit students. Content was covered very effectively and thoroughly for each lesson, with clear notes and examples. The class environment is very comfortable and it has been very enjoyable being in this tuition. Mr Lim is a wonderful tutor."</p>
      <p class="author small">Chua Hui Min Clara<br>Riverside Heights School</p>
    </article>
    <article class="card">
      <p class="quote">"Even though I have only been working with Mr Lim for a few months, I have learnt many skills and Singaporean examples that are essential for a good economics grade. Mr Lim also has amazing stories to tell, and I am inspired by his 'pilot' story."</p>
      <p class="author">Darren Seah<br>Kingsgate Institution</p>
    </article>
  </div>

  <div class="card-column col-right">
    <article class="card">
      <p class="quote small">"Mr Lim and the tuition centre has greatly improved my quality of work in economics and his knowledge and insights helped me to understand lessons well. Lessons were very valuable and I gained confidence before my exams. I would recommend this centre to anyone who wants to do well in economics."</p>
      <p class="author small">Ryan Koh<br>Ashford Junior College</p>
    </article>
    <article class="card">
      <p class="quote">"Mr Lim is a very friendly and approachable tutor who makes economic concepts much easier to understand. His lessons are well paced and effective and have raised my school test grades by 3 grades. Tuition at LessonMaple has been fun and very helpful."</p>
      <p class="author">Lee Jun Hao<br>Kingsgate Institution</p>
    </article>
    <article class="card">
      <p class="quote">"Mr Lim is a very engaging tutor who never fails to pique our interest and curiosity over economics concepts and the current economy. He makes an effort to use interesting analogies so that his students understand concepts thoroughly. Kudos!"</p>
      <p class="author">Natalie Wong Xin Yi<br>Kingsgate Institution</p>
    </article>
    <article class="card">
      <p class="quote">"I find Mr Lim a committed tutor who does research to provide us with many economics articles and practices. Group discussions and timed practices on essays and case studies let me gauge my understanding. Thanks Mr Lim!"</p>
      <p class="author">Sophia Lau Jia En<br>Harbourview Junior College</p>
    </article>
  </div>
</main>
</body>
</html>
```